Silver Lantern- We lessen the Burden

The Silver Lantern is trifold mailer. I have all but the inside of the brochure done. the front and back are designed, just not the middle. I want a testimonial that has the same background feel as the rest of the piece. I did not change the size on the art piece yet, but it will be 8.75*8.75 inches when it's folded. the piece I need you to work on is just 1 side that is 8.75*8.75. Here is the testimonial. (header)- Above Service, Beyond Compassion. (body)-“The fact that you have been trained to work with people in crisis, and that you did this of your own accord, only proves to me your
dedication and commitment to the communities we serve. When
I leave the scene of an accident or death, I know that I am leaving
the victim and their family in capable and understanding hands.”
– Dorinda Fay Oltrup
Velmore County Sheriff’s Office

Target Market(s)

funeral homes

Colors

Designer to choose colors to be used in the design.

Requirements
Must have
• The fonts that are used in the uploaded files. The concept of this piece is the Silver Lantern. I placed colored seeds on the second picture. So if a background picture is used, then I'd like it to incorporate these concepts of rebirth and continuous life-cycle
Nice to have
• Compassionate feel through the piece
Should not have
• abrasive yellow. More so the blues and purples

```html
<!DOCTYPE html>
<html lang="en">
<head>
<meta charset="utf-8">
<title>Silver Lantern – Trifold Mailer</title>
<link href="https://fonts.googleapis.com/css2?family=Oswald:wght@500&family=Tinos:ital,wght@0,400;1,400;1,700&family=Arimo&display=swap" rel="stylesheet">
<style>
  :root{
    --navy:#183259;
    --ink:#1c3560;
    --band:#172f57;
    --sky:#9dbde3;
    --mist:#c9daef;
    --paper:#ffffff;
    --text:#1e1e1e;
  }
  *{margin:0;padding:0;box-sizing:border-box}
  html,body{width:1200px;height:800px;overflow:hidden;background:var(--navy)}
  .canvas{position:relative;width:1200px;height:800px;background:var(--navy)}
  .panel{position:absolute;top:245px;width:370px;height:369px;overflow:hidden}
  .panel--cover{left:36px}
  .panel--story{left:418px;background:linear-gradient(160deg,var(--sky) 0%,var(--paper) 32%,var(--paper) 55%,var(--mist) 80%,var(--sky) 100%)}
  .panel--testimonial{left:805px;background:linear-gradient(200deg,var(--sky) 0%,var(--paper) 35%,var(--paper) 60%,var(--mist) 85%,var(--sky) 100%)}

  .cover-scene{position:absolute;inset:0;background:
    radial-gradient(ellipse 55% 38% at 50% 30%,#6f8fb8 0%,#8eaad0 55%,transparent 75%),
    linear-gradient(180deg,#a7bedc 0%,#c9d8ec 48%,#9fb5d4 62%,#7d98be 100%)}
  .cover-headline{position:absolute;top:48px;left:0;right:0;text-align:center;
    font-family:'Oswald',sans-serif;font-weight:500;font-size:38px;line-height:43px;
    color:var(--ink);letter-spacing:.5px}
  .brand{position:absolute;display:flex;align-items:center;gap:10px;
    font-family:'Tinos',serif;font-weight:400;color:var(--ink)}
  .brand__dot{width:52px;height:52px;border-radius:50%;background:var(--ink);flex:none}
  .brand__name{font-size:19px;line-height:21px}
  .panel--cover .brand{left:60px;top:248px}
  .cover-band{position:absolute;left:0;right:0;top:320px;height:33px;background:var(--band);
    color:var(--paper);font-family:'Arimo',sans-serif;font-size:19px;line-height:33px;padding-left:33px}

  .story-band{position:absolute;left:0;right:0;top:36px;height:32px;background:var(--band);
    color:var(--paper);font-family:'Tinos',serif;font-style:italic;font-size:21px;line-height:32px;text-align:center}
  .text-card{position:absolute;left:38px;width:289px;background:rgba(255,255,255,.72);border-radius:6px}
  .story-card{top:108px;height:195px;padding:20px 32px 0}
  .story-card p{font-family:'Tinos',serif;font-style:italic;font-size:8.6px;line-height:14px;color:var(--text);text-align:center}
  .story-card p+p{margin-top:14px}

  .quote-card{top:83px;height:138px;padding:34px 12px 0}
  .quote-mark{position:absolute;font-family:'Tinos',serif;font-weight:700;font-size:56px;line-height:1;color:var(--ink)}
  .quote-mark--open{left:10px;top:-4px}
  .quote-mark--close{right:12px;top:92px}
  .quote-card blockquote{font-family:'Tinos',serif;font-style:italic;font-size:8.6px;line-height:14px;color:var(--text);text-align:center}
  .quote-author{margin-top:9px;text-align:center;font-family:'Tinos',serif;font-style:italic;font-weight:700;font-size:13px;color:var(--ink)}
  .panel--testimonial .brand{left:56px;top:239px}
  .contact-band{position:absolute;left:0;right:0;top:320px;height:32px;background:var(--band);
    display:flex;align-items:center;justify-content:space-between;padding:0 12px 0 20px;color:var(--paper);
    font-family:'Tinos',serif;font-style:italic;font-weight:700}
  .contact-band__phone{font-size:25px}
  .contact-band__web{font-size:12.5px}
  .contact-strip{position:absolute;left:0;right:0;top:352px;bottom:0;background:var(--paper)}
</style>
</head>
<body>
<main class="canvas">
  <section class="panel panel--cover">
    <div class="cover-scene" role="img" aria-label="Soft blue-toned photograph of a large spreading tree in an open field under a cloudy sky"></div>
    <h1 class="cover-headline">WE’RE HERE TO<br>LESSEN THE BURDEN</h1>
    <div class="brand"><span class="brand__dot"></span><span class="brand__name">Stillwater Cleaners<br>&amp; Restoration</span></div>
    <div class="cover-band">Suicide, Homicide, Decomposition</div>
  </section>

  <section class="panel panel--story">
    <h2 class="story-band">Above Service, Beyond Compassion</h2>
    <div class="text-card story-card">
      <p>Losing a loved one is never easy, but it can be espcially difficult when the passing occurs at home. Remnats of bodily fluids can leave others exposed to hazardous conditions, if the situation is not properly dealt with.</p>
      <p>Since 1999, our locally owned trauma cleanup company has specialized in biohazard restoration and remediation for families accross Florida-- all while providing the up most in care and compassion to the families we serve. Let our family handle the cleanup while your family handles more important matters of the heart.</p>
    </div>
  </section>

  <section class="panel panel--testimonial">
    <figure class="text-card quote-card">
      <span class="quote-mark quote-mark--open">“</span>
      <blockquote>The fact that you have been trained to work with people in crisis, and that you did this of your own accord, only proves to me your dedication and commitment to the communities we serve. When I leave the scene of an accident or death, I know that I am leaving the victim and their family in capable and understanding hands.</blockquote>
      <figcaption class="quote-author">Dorinda Fay Oltrup</figcaption>
      <span class="quote-mark quote-mark--close">”</span>
    </figure>
    <div class="brand"><span class="brand__dot"></span><span class="brand__name">Stillwater Cleaners<br>&amp; Restoration</span></div>
    <div class="contact-band">
      <span class="contact-band__phone">866.555.0147</span>
      <span class="contact-band__web">www.StillwaterCleaners.com</span>
    </div>
    <div class="contact-strip"></div>
  </section>
</main>
</body>
</html>
```